Business Cards and Stationary
Silver Pine
Professional
Tom Feaster, P.G.
Founder
4718 Wexley Lane
Golden, Colorado 80401
tfeaster@silverpinenviroq.com
www.silverpinenviroq.com
Consulting Compliance Training

```html
<!DOCTYPE html>
<html lang="en">
<head>
<meta charset="utf-8">
<title>Silver Pine — Stationery Set</title>
<link rel="stylesheet" href="https://fonts.googleapis.com/css2?family=Arimo:wght@400;700&display=swap">
<style>
  :root {
    --backdrop: #6b6967;
    --paper: #ffffff;
    --brand-red: #7a1d1f;
    --ink: #3a3a3a;
    --muted: #6d6d6d;
  }
  * { margin: 0; padding: 0; box-sizing: border-box; }
  html, body { width: 1200px; height: 850px; overflow: hidden; }
  body {
    background: var(--backdrop);
    font-family: "Arimo", Arial, sans-serif;
    color: var(--ink);
    position: relative;
  }
  .sheet { position: absolute; background: var(--paper); box-shadow: 0 1px 3px rgba(0,0,0,.25); }
  .sheet--red { background: var(--brand-red); }

  .brand { display: flex; align-items: center; gap: 6px; color: var(--brand-red); font-weight: 700; text-transform: uppercase; letter-spacing: .02em; white-space: nowrap; }
  .brand__dot { border-radius: 50%; background: var(--brand-red); flex: none; }

  .address { font-style: normal; font-size: 9px; line-height: 1.35; color: var(--muted); white-space: nowrap; }
  .accent-bar { position: absolute; background: var(--brand-red); }

  /* Letterhead */
  .letterhead { left: 48px; top: 29px; width: 571px; height: 775px; }
  .letterhead .brand { position: absolute; left: 50px; top: 90px; font-size: 22px; }
  .letterhead .brand__dot { width: 14px; height: 14px; }
  .letterhead .address { position: absolute; left: 53px; top: 667px; }
  .letterhead .accent-bar { left: 53px; bottom: 26px; width: 86px; height: 10px; }

  /* Horizontal card front */
  .card-h { left: 653px; top: 43px; width: 235px; height: 132px; }
  .card-h .brand { position: absolute; left: 9px; top: 30px; font-size: 8px; gap: 3px; letter-spacing: 0; }
  .card-h .brand__dot { width: 6px; height: 6px; }
  .card-h .person { position: absolute; left: 92px; top: 22px; }
  .card-h .address { position: absolute; left: 92px; top: 68px; font-size: 6.5px; }

  .person__name { color: var(--brand-red); font-size: 8.5px; }
  .person__role { color: var(--muted); font-size: 6.5px; margin-top: 2px; }

  /* Card backs */
  .card-back { display: flex; flex-direction: column; align-items: center; justify-content: center; }
  .card-back .brand { color: var(--paper); font-size: 13px; }
  .card-back .brand__dot { background: var(--paper); width: 9px; height: 9px; }
  .card-back__web { position: absolute; color: var(--paper); font-size: 8px; }
  .card-back--h { left: 914px; top: 43px; width: 236px; height: 132px; }
  .card-back--h .card-back__web { left: 62px; bottom: 24px; }
  .card-back--v { left: 1010px; top: 202px; width: 137px; height: 242px; }
  .card-back--v .brand { font-size: 11px; }
  .card-back--v .card-back__web { right: 8px; bottom: 36px; font-size: 7px; }

  /* Vertical card fronts */
  .card-v { top: 202px; width: 149px; height: 242px; }
  .card-v--one { left: 648px; }
  .card-v--two { left: 828px; }
  .card-v .brand { position: absolute; left: 16px; top: 42px; font-size: 11px; gap: 4px; }
  .card-v .brand__dot { width: 7px; height: 7px; }
  .card-v .person { position: absolute; left: 16px; top: 112px; }
  .card-v .address { position: absolute; left: 16px; top: 178px; font-size: 6.3px; }
  .card-v .accent-bar { left: 16px; bottom: 0; width: 42px; height: 6px; }

  /* Envelope */
  .envelope { left: 432px; top: 461px; width: 720px; height: 362px; background: transparent; box-shadow: none; }
  .envelope__body { position: absolute; inset: 0; }
  .envelope .brand { position: absolute; left: 78px; top: 108px; font-size: 16px; }
  .envelope .brand__dot { width: 10px; height: 10px; }
  .envelope .address { position: absolute; left: 36px; top: 262px; font-size: 7.5px; }
  .envelope .accent-bar { left: 36px; bottom: 17px; width: 84px; height: 7px; }
</style>
</head>
<body>

  <section class="sheet letterhead" aria-label="Letterhead">
    <div class="brand"><span class="brand__dot"></span>Silver Pine</div>
    <address class="address">
      4718 Wexley Lane<br>
      Golden, Colorado 80401<br>
      Phone: 303-555-0147<br>
      www.silverpinenviroq.com
    </address>
    <div class="accent-bar"></div>
  </section>

  <section class="sheet card-h" aria-label="Business card front, horizontal">
    <div class="brand"><span class="brand__dot"></span>Silver Pine</div>
    <div class="person">
      <p class="person__name">Tom Feaster, P.G.</p>
      <p class="person__role">Founder</p>
    </div>
    <address class="address">
      4718 Wexley Lane<br>
      Golden, Colorado 80401<br>
      Phone: 303-555-0147<br>
      tfeaster@silverpinenviroq.com<br>
      www.silverpinenviroq.com
    </address>
  </section>

  <section class="sheet sheet--red card-back card-back--h" aria-label="Business card back, horizontal">
    <div class="brand"><span class="brand__dot"></span>Silver Pine</div>
    <p class="card-back__web">www.silverpinenviroq.com</p>
  </section>

  <section class="sheet card-v card-v--one" aria-label="Business card front, vertical">
    <div class="brand"><span class="brand__dot"></span>Silver Pine</div>
    <div class="person">
      <p class="person__name">Tom Feaster, P.G.</p>
      <p class="person__role">Founder</p>
    </div>
    <address class="address">
      4718 Wexley Lane<br>
      Golden, Colorado 80401<br>
      Phone: 303-555-0147<br>
      tfeaster@silverpinenviroq.com<br>
      www.silverpinenviroq.com
    </address>
    <div class="accent-bar"></div>
  </section>

  <section class="sheet card-v card-v--two" aria-label="Business card front, vertical alternate">
    <div class="brand"><span class="brand__dot"></span>Silver Pine</div>
    <div class="person">
      <p class="person__name">Tom Feaster, P.G.</p>
      <p class="person__role">Founder</p>
    </div>
    <address class="address">
      4718 Wexley Lane<br>
      Golden, Colorado 80401<br>
      Phone: 303-555-0147<br>
      tfeaster@silverpinenviroq.com<br>
      www.silverpinenviroq.com
    </address>
    <div class="accent-bar"></div>
  </section>

  <section class="sheet sheet--red card-back card-back--v" aria-label="Business card back, vertical">
    <div class="brand"><span class="brand__dot"></span>Silver Pine</div>
    <p class="card-back__web">www.silverpinenviroq.com</p>
  </section>

  <section class="sheet envelope" aria-label="Envelope">
    <svg class="envelope__body" width="720" height="362" viewBox="0 0 720 362" aria-hidden="true">
      <rect x="0" y="0" width="720" height="362" fill="#ffffff"/>
      <path d="M0 0 H720 V56 L696 72 H24 L0 56 Z" fill="#7a1d1f"/>
    </svg>
    <div class="brand"><span class="brand__dot"></span>Silver Pine</div>
    <address class="address">
      4718 Wexley Lane<br>
      Golden, Colorado 80401<br>
      Phone: 303-555-0147<br>
      www.silverpinenviroq.com
    </address>
    <div class="accent-bar"></div>
  </section>

</body>
</html>
```